Verdan Glow Banners

We need banners for our website VerdanGlow.example.
The Design must include "The Secret Japanese Skin Care System For Flawless Skin". We will need four banner sizes 300x250, 180x150, 160x600, 728x90, with our logo.

Industry/Entity Type

Paint

```html
<!DOCTYPE html>
<html lang="en">
<head>
<meta charset="utf-8">
<title>Verdan Glow – Japanese Skin Care Banner</title>
<link rel="stylesheet" href="https://fonts.googleapis.com/css2?family=Oswald:wght@300;400&family=Parisienne&family=Montserrat:wght@400;500&display=swap">
<style>
  :root {
    --canvas: #ffffff;
    --ink-grey: #8a8a8a;
    --ink-dark: #2b2b2b;
    --accent-pink: #f2a9aa;
    --panel-pink: #f5c9c8;
    --photo-light: #f7eeea;
    --photo-mid: #e9d3c9;
    --photo-dark: #c9a99a;
  }
  * { box-sizing: border-box; margin: 0; padding: 0; }
  html, body { width: 1200px; height: 148px; overflow: hidden; background: var(--canvas); }

  .banner {
    position: relative;
    width: 1200px;
    height: 148px;
    overflow: hidden;
    background: linear-gradient(180deg, #fbf6f5 0%, var(--canvas) 35%);
  }

  .banner__photo {
    position: absolute;
    left: 0; top: 0;
    width: 330px; height: 148px;
    background:
      radial-gradient(ellipse 120px 90px at 150px 70px, var(--photo-mid) 0%, transparent 75%),
      linear-gradient(90deg, var(--photo-dark) 0%, var(--photo-mid) 30%, var(--photo-light) 70%, var(--canvas) 100%);
  }

  .headline {
    position: absolute;
    left: 382px;
    top: 6px;
    color: var(--ink-grey);
  }
  .headline__lead {
    display: flex;
    align-items: baseline;
    gap: 14px;
    height: 54px;
  }
  .headline__script {
    font-family: "Parisienne", cursive;
    font-size: 40px;
    color: var(--ink-grey);
  }
  .headline__accent {
    font-family: "Oswald", sans-serif;
    font-weight: 300;
    font-size: 50px;
    letter-spacing: 1px;
    color: var(--accent-pink);
    line-height: 1;
  }
  .headline__main {
    font-family: "Oswald", sans-serif;
    font-weight: 400;
    font-size: 56px;
    line-height: 1;
    letter-spacing: 0.5px;
    color: var(--ink-grey);
    margin-top: 2px;
  }
  .headline__sub {
    font-family: "Montserrat", sans-serif;
    font-size: 19px;
    color: var(--ink-grey);
    margin-top: 2px;
  }

  .cta-panel {
    position: absolute;
    right: 0; top: 0;
    width: 272px; height: 148px;
    background: var(--panel-pink);
    color: var(--ink-dark);
    font-family: "Montserrat", sans-serif;
  }
  .cta-panel__link {
    position: absolute;
    left: 78px; top: 62px;
    display: flex;
    align-items: center;
    gap: 8px;
    font-size: 17px;
    font-weight: 500;
    letter-spacing: 0.5px;
  }
  .cta-panel__brand {
    position: absolute;
    left: 0; right: 0; top: 108px;
    text-align: center;
    font-size: 22px;
    font-weight: 400;
    letter-spacing: 4px;
    text-transform: uppercase;
  }
</style>
</head>
<body>
  <div class="banner">
    <div class="banner__photo" role="img" aria-label="Portrait photo of a smiling woman touching her cheeks with her hands"></div>

    <div class="headline">
      <div class="headline__lead">
        <span class="headline__script">the secret</span>
        <span class="headline__accent">JAPANESE</span>
      </div>
      <div class="headline__main">SKIN CARE SYSTEM</div>
      <div class="headline__sub">for flawless skin</div>
    </div>

    <div class="cta-panel">
      <div class="cta-panel__link">
        READ MORE
        <svg width="11" height="13" viewBox="0 0 11 13" aria-hidden="true"><path d="M0 0 L11 6.5 L0 13 Z" fill="#2b2b2b"/></svg>
      </div>
      <div class="cta-panel__brand">Verdan Glow</div>
    </div>
  </div>
</body>
</html>
```